Breezeway Climate Business Card Design

Design new, 2 sides, business cards for a residential and light commercial heating, air conditioning contractor.

Target Market(s)

Homeowners, small businesses

Industry/Entity Type

Business

Contact Information for Business Card

Dominic Vasquerelli
Phone - 555-214-6837
Email
Address - PO box 618
Millbrook NJ 07999
Website - www.BreezewayClimateLLC.example

Requirements
Must have
• logo, company colors, standard size with no die cut, so I can use printhaven

```html
<!DOCTYPE html>
<html lang="en">
<head>
<meta charset="utf-8">
<title>Breezeway Climate Business Card</title>
<link href="https://fonts.googleapis.com/css2?family=Open+Sans:wght@400;600&display=swap" rel="stylesheet">
<style>
  :root {
    --backdrop: #5b5b5b;
    --card-white: #ffffff;
    --maroon: #9b1f32;
    --maroon-deep: #7a2030;
    --cream: #f6dfa0;
    --ink: #222222;
    --icon-red: #e3262c;
    --rule: #333333;
  }
  * { margin: 0; padding: 0; box-sizing: border-box; }
  html, body {
    width: 1200px; height: 1200px; overflow: hidden;
    background: var(--backdrop);
    font-family: "Open Sans", sans-serif;
  }
  .card {
    position: absolute; left: 255px; width: 689px; height: 391px; overflow: hidden;
  }
  .card-front { top: 178px; background: var(--card-white); }
  .card-back { top: 630px; background: var(--maroon-deep); }

  .brand {
    position: absolute; display: flex; align-items: center; gap: 8px;
    font-weight: 600; white-space: nowrap;
  }
  .brand-mark { border-radius: 50%; flex: none; }
  .card-front .brand {
    left: 159px; top: 206px; transform: translate(-50%, -50%);
    font-size: 22px; color: var(--maroon);
  }
  .card-front .brand-mark { width: 18px; height: 18px; background: var(--maroon); }
  .card-back .brand {
    left: 345px; top: 194px; transform: translate(-50%, -50%);
    font-size: 32px; color: var(--cream);
  }
  .card-back .brand-mark { width: 26px; height: 26px; background: var(--cream); }

  .divider {
    position: absolute; left: 313px; top: 75px; width: 1.5px; height: 240px;
    background: var(--rule);
  }
  .name-band {
    position: absolute; left: 313px; top: 105px; width: 376px; height: 57px;
    background: var(--maroon);
    display: flex; align-items: center; padding-left: 14px;
  }
  .name {
    color: var(--cream); font-size: 24px; font-weight: 400; letter-spacing: 0.2px;
  }
  .contact-list {
    position: absolute; left: 327px; top: 183px; list-style: none;
    color: var(--ink); font-size: 15px; line-height: 23px;
  }
  .contact-list li { display: flex; align-items: center; gap: 6px; white-space: nowrap; }
  .contact-list svg { width: 17px; height: 14px; flex: none; }
  .address {
    position: absolute; left: 327px; top: 271px;
    color: var(--ink); font-size: 16px; white-space: nowrap;
  }
  .website-back {
    position: absolute; left: 0; right: 0; top: 342px; text-align: center;
    color: #ffffff; font-size: 17px;
  }
</style>
</head>
<body>
  <section class="card card-front">
    <div class="brand"><span class="brand-mark"></span>Breezeway Climate</div>
    <div class="divider"></div>
    <div class="name-band"><h1 class="name">Dominic Vasquerelli</h1></div>
    <ul class="contact-list">
      <li>
        <svg viewBox="0 0 17 14" aria-hidden="true"><path fill="var(--icon-red)" d="M1 4 Q8.5 -1 16 4 L14 6 L11 5 L11 3.5 Q8.5 2.6 6 3.5 L6 5 L3 6 Z M4 7 L13 7 L15 13 L2 13 Z"/><circle cx="8.5" cy="10" r="1.8" fill="#fff"/></svg>
        555-214-6837
      </li>
      <li>
        <svg viewBox="0 0 17 14" aria-hidden="true"><rect x="1" y="2" width="15" height="10" fill="var(--icon-red)"/><path d="M1 2 L8.5 8 L16 2 M1 12 L6.5 6.5 M16 12 L10.5 6.5" stroke="#fff" stroke-width="1.2" fill="none"/></svg>
        d.vasquerelli@BreezewayClimateLLC.example
      </li>
      <li>
        <svg viewBox="0 0 17 14" aria-hidden="true"><g fill="none" stroke="var(--icon-red)" stroke-width="1.2"><circle cx="8.5" cy="7" r="6"/><ellipse cx="8.5" cy="7" rx="2.6" ry="6"/><path d="M2.5 7 H14.5 M3.5 4 H13.5 M3.5 10 H13.5"/></g></svg>
        www.BreezewayClimateLLC.example
      </li>
    </ul>
    <p class="address">PO box 618 Millbrook NJ 07999</p>
  </section>

  <section class="card card-back">
    <div class="brand"><span class="brand-mark"></span>Breezeway Climate</div>
    <p class="website-back">www.BreezewayClimateLLC.example</p>
  </section>
</body>
</html>
```